Business Card Design for Animal Clinic

We are seeking a two sided business card design. The primary side should include our logo (provided in AI and EPS files) address, phone, website, and if possible "Follow Us" with icons for Facebook, Google+, and Twitter.

The back of the card needs to included space for appointment reminders.

Company Name:
Calderbrook Animal Clinic

Doctor Name:
To be provided to winner

Adress:
To be provided to winner

Phone:
to be provided to winner

Website:
www.calderbrookanimalclinic.com

```html
<!DOCTYPE html>
<html lang="en">
<head>
<meta charset="utf-8">
<title>Calderbrook Animal Clinic – Business Card</title>
<link rel="stylesheet" href="https://fonts.googleapis.com/css2?family=Federo&family=Libre+Baskerville:wght@700&family=Courier+Prime:wght@700&family=Arimo:wght@700&display=swap">
<style>
  :root {
    --backdrop: #aabab7;
    --clinic-red: #a51c21;
    --frame-red: #b3262a;
    --band-black: #0b0b0c;
    --paper: #ffffff;
    --text-light: #f4f4f4;
  }
  * { box-sizing: border-box; margin: 0; padding: 0; }
  html, body {
    width: 1200px; height: 900px; overflow: hidden;
    background: var(--backdrop);
  }
  .canvas { position: relative; width: 1200px; height: 900px; }

  .card {
    position: absolute; left: 191px; width: 816px;
    background: var(--frame-red);
    padding: 10px 11px;
  }
  .card--front { top: 0; height: 437px; }
  .card--back { top: 464px; height: 434px; }

  .card__inner { position: relative; width: 100%; height: 100%; background: var(--paper); }

  .brand-name {
    position: absolute; left: 0; right: 0; text-align: center;
    font-family: "Federo", sans-serif; font-weight: 400;
    color: var(--clinic-red); line-height: 1;
  }
  .card--front .brand-name--main { top: 38px; font-size: 92px; letter-spacing: 3px; }
  .card--front .brand-name--sub { top: 180px; font-size: 44px; letter-spacing: 10px; }
  .card--back .brand-name--main { top: 22px; font-size: 66px; letter-spacing: 2px; }
  .card--back .brand-name--sub { top: 80px; font-size: 34px; letter-spacing: 6px; }

  .contact-band {
    position: absolute; left: 0; right: 0; bottom: 0;
    background: var(--band-black); color: var(--text-light);
    text-align: center;
  }
  .card--front .contact-band { height: 104px; padding-top: 12px; }
  .address {
    font-family: "Libre Baskerville", serif; font-weight: 700; font-size: 19px;
  }
  .phone-row {
    display: flex; justify-content: center; align-items: center; gap: 40px;
    margin-top: 6px;
  }
  .phone {
    font-family: "Courier Prime", monospace; font-weight: 700; font-size: 25px;
    letter-spacing: 1px;
  }
  .cross-icon { width: 20px; height: 20px; display: block; }
  .website {
    font-family: "Arimo", sans-serif; font-weight: 700; font-size: 20px;
    margin-top: 4px;
  }

  .header-rule {
    position: absolute; left: 0; right: 0; top: 112px; height: 3px;
    background: var(--frame-red);
  }
  .appointment-area { position: absolute; left: 0; right: 0; top: 115px; height: 199px; }
  .card--back .contact-band { height: 100px; }
</style>
</head>
<body>
<div class="canvas">

  <section class="card card--front" aria-label="Business card front">
    <div class="card__inner">
      <h1 class="brand-name brand-name--main">CALDERBROOK</h1>
      <p class="brand-name brand-name--sub">ANIMAL CLINIC</p>

      <div class="contact-band">
        <p class="address">418 N. Harlow Lane, Brookfield Springs, FL 32099</p>
        <div class="phone-row">
          <svg class="cross-icon" viewBox="0 0 20 20" aria-hidden="true">
            <path d="M7 0h6v7h7v6h-7v7H7v-7H0V7h7z" fill="var(--frame-red)"/>
          </svg>
          <p class="phone">(555) 014-2738</p>
          <svg class="cross-icon" viewBox="0 0 20 20" aria-hidden="true">
            <path d="M7 0h6v7h7v6h-7v7H7v-7H0V7h7z" fill="var(--frame-red)"/>
          </svg>
        </div>
        <p class="website">www.calderbrookanimalclinic.com</p>
      </div>
    </div>
  </section>

  <section class="card card--back" aria-label="Business card back">
    <div class="card__inner">
      <h2 class="brand-name brand-name--main">CALDERBROOK</h2>
      <p class="brand-name brand-name--sub">ANIMAL CLINIC</p>
      <div class="header-rule"></div>
      <div class="appointment-area" aria-label="Space for appointment reminders"></div>
      <div class="contact-band"></div>
    </div>
  </section>

</div>
</body>
</html>
```